Laboratory Pain Managment Brochure

I want a simple easy to read brochure for doctors. My toxicology lab is in the pain management arena. We provide urine drug monitoring to ensure patients are taking their medication properly. I would like a few photos of adults, doctors, nurses and a happy family. Also, feel free to add a logo that would describe this type of testing

Running theme like " Successfully serving North Dakota since 1996 "

Cover Page # 1

Brilliant photo with Corvella Diagnostics

Would like a running theme of being Corvella being a North Dakota based lab

Page # 2

Corvella Labs has been successfully serving North Dakota since 1996. Dr. Gavin Tellemy, President of Corvella Lab, has over 25 years of medical experience doing research for Brindle University and The University of Parkmoor. In addition, he has worked with clinics giving him a comprehensive understanding of drug testing. It is Corvella Lab mission to supply the best service for our costumers by understanding their needs so they can provide the best possible patient care.

Corvella Features:
•24 – 48 Hour Turnaround Time
•Customer Satisfaction is Our Number 1 Priority
•Capable of Billing all Major Insurance Companies
•Thorough Drug Testing Capabilities Including K2/Spice testing
•Apply Lean Process Control to Supply the best Quality of Analysis
•Easy and Convenient Web-based Interface
•Easy and Customizable Reporting
-The Vexlo is state of the art technology that uses ion entrapment to give better quantitative results. This gives us the ability to detect for more drugs at a higher accuracy.

Why test: Page # 2

Why Monitor Prescription Drug Usage? Prescription drug abuse is the use of medication without a prescription, in a way other than prescribed, or for the experience or feeling elicited. According to several national surveys, prescription medications, such as those used to treat pain, attention deficit disorders, and anxiety, are being abused at a rate second only to marijuana among illicit drug users. The consequences of this abuse have been steadily worsening, reflected in increased treatment admissions, emergency room visits, and overdose deaths.

Can you tell if your patient is taking his/her medication properly?
Even though monitoring your patients behavior is important it is not adequate to know if the patient is misusing their medications. Monitoring the patients behavior as well as drug monitoring testing will give you the most insight into your patients drug usage.

There are many reasons why pain patients may not be taking their medication as prescribed:
•Due to fear of addiction will not take the medication.
•Compulsive use because of addiction.
•Sell the medication to someone else for profit.
•Abuse the medication intentionally

FWRAB's Dosage Integrity Safeguard Plan
The 2011 Dosage Integrity Safeguard Plan expands upon the Harlow Administration's Federal Substance Oversight Agenda and includes action in four major areas to reduce prescription drug abuse:

•Education. A crucial first step in tackling the problem of prescription drug abuse is to educate parents, youth, and patients about the dangers of abusing prescription drugs, while requiring prescribers to receive education on the appropriate and safe use, and proper storage and disposal of prescription drugs.
•Monitoring. Implement prescription drug monitoring programs (PDMPs) in every state to reduce “doctor shopping” and diversion, and enhance PDMPs to make sure they can share data across states and are used by healthcare providers.
•Proper Medication Disposal. Develop convenient and environmentally responsible prescription drug disposal programs to help decrease the supply of unused prescription drugs in the home.
•Enforcement. Provide law enforcement with the tools necessary to eliminate improper prescribing practices and stop pill mills.

References
1.(2011, October). Retrieved November 2012, from BSRC: Bureau of Substance Research Councils: http://www.example-substancebureau.test/sites/default/files/rrdosage.pdf
2.Commun Care Rev. 2009 Aug;12(4):185-90. doi: 10.1089/pop.2009.0015
3. http://www.example-federaloffice.test/fwrab/dosage-integrity

Page # 3 a list of all four panels we offer....... see attachment and use title of panel in the tabs at the bottom of the excel sheet

Back cover Page # 4 ..... brilliant picture..... North Dakota based lab

Corvella Diagnostics, Inc.
482 Larkfield Ave. E
Williston, ND 58934
ph: (701) 555-0143
www.corvellalab.test

I have removed one stat and added another...... please see the references section

Thank you

Target Market(s)

Pain Managment doctors, internal medicine doctors, general practioners, nuerologist, rehab centers, detox facility, hospitals, just about any doctor that prescribes schedule 2 narcotics

Industry/Entity Type

Healthcare

Requirements
Must have
• Back page I want the family picture with a caption reading

We view your patients like family

```html
<!DOCTYPE html>
<html lang="en">
<head>
<meta charset="utf-8">
<title>Corvella Diagnostics – Brochure Cover</title>
<link href="https://fonts.googleapis.com/css2?family=Arimo:wght@400;700&display=swap" rel="stylesheet">
<style>
  :root {
    --backdrop: #3a3a3a;
    --paper: #ffffff;
    --brand-blue: #1a8fd6;
    --brand-blue-light: #3ab4ec;
    --brand-green: #7cbf3a;
    --brand-green-light: #9ad14d;
    --band-shadow: #d9dde2;
    --photo-cool: #9fc4de;
    --photo-steel: #c7d9e7;
    --photo-coat: #f4f7fa;
    --photo-skin: #e9dccf;
    --photo-deep: #6f9dbf;
  }
  * { box-sizing: border-box; margin: 0; padding: 0; }
  html, body {
    width: 1200px;
    height: 750px;
    overflow: hidden;
    background: var(--backdrop);
    font-family: "Arimo", Arial, sans-serif;
  }
  .cover {
    position: absolute;
    left: 350px;
    top: 25px;
    width: 500px;
    height: 700px;
    background: var(--paper);
    box-shadow: 0 10px 30px rgba(0,0,0,0.45);
    overflow: hidden;
  }
  .cover-art {
    position: absolute;
    left: 0;
    top: 0;
    width: 500px;
    height: 700px;
  }
  .brand {
    position: absolute;
    top: 62px;
    right: 34px;
    display: flex;
    align-items: center;
    gap: 8px;
  }
  .brand-dot {
    width: 22px;
    height: 22px;
    border-radius: 50%;
    background: var(--brand-blue);
  }
  .brand-name {
    font-weight: 700;
    font-size: 20px;
    color: var(--brand-blue);
  }
  .web-address {
    position: absolute;
    left: 24px;
    top: 419px;
    font-size: 10px;
    letter-spacing: 2.4px;
    color: var(--paper);
    transform: rotate(4.2deg);
    transform-origin: left center;
  }
  .tagline {
    position: absolute;
    left: 150px;
    top: 540px;
    font-size: 27px;
    font-weight: 400;
    line-height: 1.15;
    color: var(--brand-blue);
  }
</style>
</head>
<body>
  <main class="cover">
    <svg class="cover-art" viewBox="0 0 500 700" xmlns="http://www.w3.org/2000/svg">
      <defs>
        <linearGradient id="labPhotoTone" x1="0" y1="0" x2="1" y2="0.6">
          <stop offset="0" stop-color="var(--photo-cool)"/>
          <stop offset="0.22" stop-color="var(--photo-steel)"/>
          <stop offset="0.45" stop-color="var(--photo-coat)"/>
          <stop offset="0.62" stop-color="var(--photo-skin)"/>
          <stop offset="0.8" stop-color="var(--photo-coat)"/>
          <stop offset="1" stop-color="var(--photo-deep)"/>
        </linearGradient>
        <linearGradient id="blueBand" x1="0" y1="0" x2="1" y2="0">
          <stop offset="0" stop-color="var(--brand-blue-light)"/>
          <stop offset="1" stop-color="var(--brand-blue)"/>
        </linearGradient>
        <linearGradient id="greenBand" x1="0" y1="0" x2="1" y2="0">
          <stop offset="0" stop-color="var(--brand-green-light)"/>
          <stop offset="1" stop-color="var(--brand-green)"/>
        </linearGradient>
      </defs>

      <polygon class="lab-photo" role="img"
               aria-label="Photo of laboratory scientists in white coats and safety glasses working with a microscope and pipette"
               points="0,158 500,158 500,446 300,434 0,412" fill="url(#labPhotoTone)"/>

      <rect class="band-top-blue" x="110" y="146" width="320" height="12" fill="url(#blueBand)"/>
      <rect class="band-top-green" x="430" y="152" width="70" height="12" fill="url(#greenBand)"/>

      <polygon class="band-shadow" points="0,440 300,462 500,478 500,486 300,470 0,448" fill="var(--band-shadow)"/>
      <polygon class="band-bottom-green" points="0,410 300,432 300,462 0,440" fill="url(#greenBand)"/>
      <polygon class="band-bottom-blue" points="300,432 500,444 500,478 300,462" fill="url(#blueBand)"/>
    </svg>

    <div class="brand">
      <span class="brand-dot"></span>
      <span class="brand-name">Corvella Lab</span>
    </div>

    <p class="web-address">www.corvellalab.test</p>

    <h1 class="tagline">Successfully serving<br>North Dakota since 1996</h1>
  </main>
</body>
</html>
```